Clean Chic Simple Black & White One sided Biz Card

I need a business card for my company Brief Matter Arrangers. We are a luxury, white glove service for organizing files for attorneys.
I would like something that is stunningly simple and chic/sexy. This is going to be only one sided. We are going to use raised ink or ink embossing for the printing. So the logo will be raised in black. I am currently waiting to hear back from the printer as to whether or not the logo has to be in all black or can be left in its current state of black with grey initials. Please check our website for inspiration. www.briefmatterarrangers.example.
Thank you so much for your time.

* Please decide whichever title you think looks best(Chief Executive Officer, CEO, or President)
Updates

I really like the designs that make the logo large and the main focus.  
I also like the use of modern, masculine, simple, chic fonts for the slogan and info.

1) No bold font on slogan or info
2) Shrink info to be smaller maybe to make the logo bigger and more the focus
3) Maybe use grey for all the info and slogan so the focus will be on the logo

Thank you so much for your time!!

Target Market(s)

Luxury driven lawyers and their support staff

Industry/Entity Type

Printer

Requirements
Must have
• One sided card

Modern, sleek, masculine, chic, simple font.

Please add our slogan. Refer to file labeled "old logo" to see how we added our slogan under the old logo.
The slogan is, "We Bring Calm to Every Legal Brief"

Please include the info below:
Marion Tullbeck (Chief Executive Officer, CEO, or President)
812 North Halvering Avenue, Suite 1400
Westmere, California 90614
P: (213)555-0182 F: (213)555-0167
mariont@briefmatterarrangers.example
www.briefmatterarrangers.example

Please refer to attached file labeled "inkpressingembossing requirements" for requirements from my printer. Thank you!
Nice to have
• It can be super simple with just the logo and my info. Or it could maybe have some cool feature. Just clean please.

I would prefer the info not be in bold. I think this will help the Logo stand out as the main focus.

I attached files of how the ink pressing and embossing will look.
Should not have
• No crazy shapes and no color other than black with a white background. The logo should be the focus since it will be embossed.

```html
<!DOCTYPE html>
<html lang="en">
<head>
<meta charset="utf-8">
<title>Brief Matter Arrangers — Business Card</title>
<link rel="stylesheet" href="https://fonts.googleapis.com/css2?family=Cinzel:wght@700&family=Tinos:ital@1&family=Arimo:wght@400&display=swap">
<style>
  :root {
    --paper: #ffffff;
    --ink: #111111;
    --slogan: #3a3a3a;
    --accent-grey: #a9b8b8;
    --band: #d2d2d2;
    --info: #1a1a1a;
  }
  html, body {
    margin: 0;
    padding: 0;
    width: 1200px;
    height: 656px;
    overflow: hidden;
    background: var(--paper);
  }
  .card {
    position: relative;
    width: 1200px;
    height: 656px;
    background: var(--paper);
    overflow: hidden;
  }
  .brand-mark {
    position: absolute;
    left: 0;
    top: 0;
    width: 1200px;
    height: 356px;
  }
  .brand-mark__shape {
    position: absolute;
    left: 532px;
    top: 32px;
    width: 140px;
    height: 140px;
    border-radius: 50%;
    background: var(--accent-grey);
  }
  .brand-mark__name {
    position: absolute;
    left: 0;
    width: 1200px;
    top: 226px;
    margin: 0;
    text-align: center;
    font-family: "Cinzel", "Times New Roman", serif;
    font-weight: 700;
    font-size: 31px;
    letter-spacing: 0.26em;
    color: var(--ink);
    line-height: 1;
  }
  .slogan {
    position: absolute;
    left: 0;
    width: 1200px;
    top: 274px;
    margin: 0;
    text-align: center;
    font-family: "Tinos", "Times New Roman", serif;
    font-style: italic;
    font-size: 29px;
    color: var(--slogan);
    line-height: 1;
  }
  .info-band {
    position: absolute;
    left: 0;
    top: 356px;
    width: 1200px;
    height: 300px;
    background: var(--band);
  }
  .info-panel {
    position: absolute;
    left: 14px;
    top: 14px;
    width: 1162px;
    height: 262px;
    border: 5px solid var(--paper);
    background: var(--band);
    font-family: "Arimo", Arial, sans-serif;
    color: var(--info);
  }
  .person {
    position: absolute;
    left: 30px;
    top: 70px;
  }
  .person__name {
    margin: 0;
    font-size: 40px;
    font-weight: 400;
    letter-spacing: -0.03em;
    line-height: 1;
  }
  .person__title {
    margin: 8px 0 0;
    font-size: 27px;
    letter-spacing: -0.02em;
    line-height: 1;
  }
  .contact {
    position: absolute;
    right: 24px;
    top: 26px;
    margin: 0;
    text-align: right;
    font-style: normal;
    font-size: 29px;
    line-height: 39px;
    letter-spacing: -0.005em;
  }
  .contact span { display: block; }
</style>
</head>
<body>
  <div class="card">
    <header class="brand-mark">
      <div class="brand-mark__shape"></div>
      <h1 class="brand-mark__name">Brief Matter Arrangers, Inc.</h1>
      <p class="slogan">“We Bring Calm to Every Legal Brief”</p>
    </header>

    <section class="info-band">
      <div class="info-panel">
        <div class="person">
          <p class="person__name">MARION TULLBECK</p>
          <p class="person__title">President</p>
        </div>
        <address class="contact">
          <span>812 North Halvering Avenue, Suite 1400</span>
          <span>Westmere, California 90614</span>
          <span>P: (213)555-0182 F: (213)555-0167</span>
          <span>mariont@briefmatterarrangers.example</span>
          <span>www.briefmatterarrangers.example</span>
        </address>
      </div>
    </section>
  </div>
</body>
</html>
```